Ductless Mini Split Business Website

Tall Fern Services is looking to design an eye catching educational website about installing Ductless mini splits.

Similar to this company.
https://www.kelvarocomfort.com/

```html
<!DOCTYPE html>
<html lang="en">
<head>
<meta charset="utf-8">
<title>Tall Fern Services – Ductless Experts</title>
<link href="https://fonts.googleapis.com/css2?family=Poppins:wght@300;400;500;600;700&family=Montserrat:wght@800;900&display=swap" rel="stylesheet">
<style>
:root{
  --yellow:#ffd200;
  --black:#000;
  --dark:#1b1b1b;
  --ink:#222;
  --muted:#8a8a8a;
  --line:#e4e4e4;
  --soft:#f4f4f5;
  --white:#fff;
}
*{box-sizing:border-box;margin:0;padding:0}
html,body{width:1200px;height:3957px;overflow:hidden}
body{position:relative;font-family:'Poppins',sans-serif;color:var(--ink);background:var(--white)}
.abs{position:absolute}
svg{display:block}

/* top bar */
.topbar{left:0;top:0;width:1200px;height:37px;background:var(--black);color:#fff;font-size:11px}
.topbar .tagline{left:173px;top:11px}
.topbar .social{left:718px;top:13px;display:flex;gap:9px}
.topbar .social span{width:9px;height:9px;background:#fff;border-radius:1px}
.topbar .call{left:825px;top:0;width:375px;height:37px;background:var(--yellow);color:#000;font-size:11px;display:flex;align-items:center;gap:6px;padding-left:12px}

/* header */
.brand{display:flex;align-items:center;gap:8px}
.brand .dot{width:22px;height:22px;border-radius:50%;background:var(--yellow)}
.brand .name{font-weight:700;font-size:19px;color:var(--black);line-height:1}
.brand-sub{font-weight:600;font-size:12px;letter-spacing:.3px}
.contact-mini{display:flex;gap:14px;align-items:flex-start}
.sq-icon{width:33px;height:33px;background:var(--yellow);display:flex;align-items:center;justify-content:center}
.contact-mini b{display:block;font-weight:400;font-size:12px;color:#333}
.contact-mini small{font-size:10px;color:var(--muted)}

/* nav */
.nav{left:171px;top:131px;width:856px;height:47px;background:#fff;box-shadow:0 2px 10px rgba(0,0,0,.12);z-index:5;display:flex;align-items:center;padding-left:13px;font-size:11.5px;font-weight:500;letter-spacing:.3px}
.nav a{color:#111;text-decoration:none;margin-right:35px}
.nav a.active{color:var(--yellow)}
.nav .appt{margin-left:auto;padding-left:20px;border-left:1px solid var(--line);display:flex;gap:10px;align-items:center;font-weight:600;margin-right:13px;font-size:12px}

/* hero */
.hero{left:0;top:154px;width:1200px;height:533px;background:linear-gradient(90deg,#f1f1f1 0%,#e8e6e3 45%,#cfcac4 75%,#a9a6a3 100%)}
.hero .badge{left:171px;top:129px;width:202px;height:32px;background:var(--yellow);font-size:13px;display:flex;align-items:center;justify-content:center;letter-spacing:.4px}
.hero h1{left:171px;top:190px;font-family:'Montserrat',sans-serif;font-weight:900;font-size:49px;line-height:70px;color:#151515;letter-spacing:.5px}
.hero .btn{left:175px;top:346px;width:134px;height:49px;border:2px solid #222;font-size:14px;display:flex;align-items:center;justify-content:center}
.hero .arrow{top:244px;width:37px;height:46px;background:#222;display:flex;align-items:center;justify-content:center}

/* section heads */
.label{font-size:10px;color:var(--muted);letter-spacing:.5px;text-transform:uppercase}
.head-bar{border-left:4px solid var(--yellow);padding-left:19px}
.title{font-size:27px;font-weight:500;color:#111;line-height:1.2}
.para{font-size:12.5px;line-height:22px;color:var(--muted)}

/* about */
.feature-box{left:171px;width:418px;height:69px;border:1px solid var(--line);display:flex;align-items:center;gap:16px;padding-left:12px;font-size:15px;color:#222}
.photo{background:linear-gradient(135deg,#d9d4cc,#a8a39b)}

/* services */
.services{left:0;top:1296px;width:1200px;height:678px;background:var(--black);color:#fff}
.services .label{color:#fff;text-align:center;width:1200px;top:72px}
.services .title{color:#fff;text-align:center;width:1200px;top:100px;font-size:27px}
.services .uline{left:573px;top:145px;width:54px;height:4px;background:var(--yellow)}
.card{width:198px;height:157px;background:#fff;color:#111}
.card .img{height:106px;background:linear-gradient(135deg,#e9e9e9,#b7bcc2)}
.card .cap{height:51px;display:flex;align-items:center;justify-content:center;text-align:center;font-size:14px;line-height:1.4}
.services .more{left:516px;top:593px;width:166px;height:37px;background:var(--yellow);color:#000;font-size:12px;display:flex;align-items:center;justify-content:center}

/* why */
.why-item{display:flex;align-items:center;gap:14px;font-size:12.5px;font-weight:600}
.why-item .sq-icon{width:34px;height:34px}

.contact-card{left:171px;top:2379px;width:402px;height:415px;background:#fff;box-shadow:0 4px 14px rgba(0,0,0,.14)}
.contact-card h3,.quote h3{font-size:19px;font-weight:600;position:absolute;left:35px;top:28px}
.c-row{left:35px;width:330px;display:flex;align-items:center;gap:24px;font-size:17px;color:#999;font-weight:300;padding-bottom:14px}
.c-row .sq-icon{width:41px;height:41px}
.c-sep{left:35px;width:330px;border-top:2px dotted #bbb}

.quote{left:612px;top:2379px;width:398px;height:415px;background:var(--black);color:#fff}
.quote h3{left:25px}
.field{left:27px;width:343px;height:29px;border:1px solid #555;background:#111;color:#777;font-size:10px;padding:8px 14px}
.quote .submit{left:27px;top:353px;width:343px;height:36px;background:var(--yellow);color:#000;font-size:14px;display:flex;align-items:center;justify-content:center}

.promo{top:2863px;width:270px;height:195px;background:linear-gradient(135deg,#ece9e4,#c7c0b5)}
.promo .bar{position:absolute;left:0;bottom:0;width:100%;height:57px;background:var(--yellow);display:flex;align-items:center;justify-content:space-between;padding:0 9px 0 16px;font-weight:600;font-size:16.5px;letter-spacing:.5px}
.promo .play{width:31px;height:31px;background:#111;display:flex;align-items:center;justify-content:center}

/* testimonials */
.testimonials{left:0;top:3127px;width:1200px;height:458px;background:var(--soft)}
.t-photo{left:258px;top:63px;width:318px;height:303px;border:7px solid var(--yellow);background:linear-gradient(135deg,#fff 0%,#fff 60%,#eee 60%);overflow:hidden}
.t-photo .fill{position:absolute;left:0;top:0;width:100%;height:100%;background:linear-gradient(135deg,#f7f7f7 0%,#e2e2e2 60%,var(--yellow) 60.2%)}
.t-name{left:612px;top:307px;display:flex;align-items:center;gap:12px;font-size:12.5px;color:#333}
.t-name i{width:72px;border-top:1px solid #888}
.t-arrow{top:364px;width:29px;height:29px;background:#111;display:flex;align-items:center;justify-content:center}

/* footer */
.footer{left:0;top:3585px;width:1200px;height:320px;background:var(--dark);color:#fff}
.footer h4{font-size:16.5px;font-weight:600;position:absolute;top:68px}
.footer h4::after{content:"";position:absolute;left:0;top:27px;width:40px;height:2px;background:var(--yellow)}
.f-text{font-size:11.5px;line-height:19px;color:#aaa}
.f-list{list-style:none;font-size:11.5px;line-height:23px;color:#aaa}
.f-list li::before{content:"";display:inline-block;width:4px;height:4px;border-radius:50%;background:var(--yellow);margin-right:6px;vertical-align:middle}
.f-social{left:171px;top:226px;display:flex;gap:6px}
.f-social span{width:29px;height:28px;background:#3a5aa8}
.f-social span:nth-child(2){background:#2a9bd8}
.f-social span:nth-child(3){background:#c8463a}
.f-social span:nth-child(4){background:#2672b0}
.f-input{left:756px;top:167px;width:271px;height:30px;border:1px solid #555;background:#2a2a2a;font-size:10px;color:#888;padding:9px 14px}
.f-btn{left:756px;top:204px;width:271px;height:29px;background:var(--yellow);color:#000;font-size:12px;display:flex;align-items:center;justify-content:center}
.copyright{left:0;top:3905px;width:1200px;height:52px;background:var(--black);color:#fff;font-size:12px;padding:18px 0 0 171px}
</style>
</head>
<body>

<!-- top bar -->
<div class="abs topbar">
  <div class="abs tagline">Your Trusted 24 Hours Service Provider</div>
  <div class="abs social"><span></span><span></span><span></span><span></span></div>
  <div class="abs call">
    <svg width="11" height="11" viewBox="0 0 24 24"><path d="M6.6 10.8a15 15 0 0 0 6.6 6.6l2.2-2.2c.3-.3.7-.4 1-.2 1.1.4 2.3.6 3.6.6.6 0 1 .4 1 1V20c0 .6-.4 1-1 1A17 17 0 0 1 3 4c0-.6.4-1 1-1h3.5c.6 0 1 .4 1 1 0 1.3.2 2.5.6 3.6.1.3 0 .7-.2 1z" fill="#000"/></svg>
    <span>Call Us Today &nbsp;000 - 000 - 000</span>
  </div>
</div>

<!-- header -->
<header>
  <div class="abs" style="left:210px;top:56px">
    <div class="brand"><span class="dot"></span><span class="name">Tall Fern Services</span></div>
    <div class="brand-sub" style="margin:8px 0 0 4px">DUCTLESS EXPERTS</div>
  </div>
  <div class="abs contact-mini" style="left:661px;top:66px">
    <div class="sq-icon"><svg width="14" height="11" viewBox="0 0 24 18"><rect x="1" y="1" width="22" height="16" fill="#111"/><path d="M1 1l11 9 11-9" stroke="#ffd200" stroke-width="2" fill="none"/></svg></div>
    <div><b>Email</b><small>info@tallfern.com</small></div>
  </div>
  <div class="abs contact-mini" style="left:844px;top:66px">
    <div class="sq-icon"><svg width="11" height="15" viewBox="0 0 16 22"><path d="M8 0a8 8 0 0 0-8 8c0 6 8 14 8 14s8-8 8-14a8 8 0 0 0-8-8z" fill="#111"/><circle cx="8" cy="8" r="3" fill="#ffd200"/></svg></div>
    <div><b>Address</b><small>18 Larch Ave, Portland, USA</small></div>
  </div>
</header>

<nav class="abs nav">
  <a class="active">HOME</a><a>ABOUT US</a><a>DUCTLESS</a><a>FAQ</a><a>FINANCING</a><a>REVIEWS</a><a>CONTACT US</a>
  <span class="appt">
    <svg width="16" height="15" viewBox="0 0 24 22"><rect x="1" y="3" width="22" height="18" fill="none" stroke="#ffd200" stroke-width="2"/><rect x="1" y="3" width="22" height="5" fill="#ffd200"/><path d="M6 0v5M18 0v5" stroke="#ffd200" stroke-width="2"/></svg>
    Make An Appointment
  </span>
</nav>

<!-- hero -->
<section class="abs hero" role="img" aria-label="Bright living room with a wall-mounted ductless unit and a family relaxing on a sofa">
  <div class="abs badge">WE ARE EXPERTS</div>
  <h1 class="abs">INSTALLING DUCTLESS<br>MINI SPLITS</h1>
  <div class="abs btn">READ MORE</div>
  <div class="abs arrow" style="left:60px"><svg width="12" height="22" viewBox="0 0 12 22"><path d="M11 1L1 11l10 10" stroke="#fff" stroke-width="1.5" fill="none"/></svg></div>
  <div class="abs arrow" style="left:1103px"><svg width="12" height="22" viewBox="0 0 12 22"><path d="M1 1l10 10L1 21" stroke="#fff" stroke-width="1.5" fill="none"/></svg></div>
</section>

<!-- about -->
<section>
  <div class="abs head-bar" style="left:171px;top:786px">
    <div class="label">Who we are</div>
    <div class="title">About Tall Fern</div>
  </div>
  <p class="abs para" style="left:171px;top:860px;width:410px;font-size:11.5px">Nemo enim ipsam voluptatem quia voluptas sit aspernatur aut odit aut fugit, sed quia consequuntur magni dolores eos qui ratione voluptatem sequi nesciunt. Neque porro quisquam est qui dolorem ipsum quia dolor sit amet .</p>
  <div class="abs feature-box" style="top:971px"><svg width="15" height="13" viewBox="0 0 16 14"><rect x="1" y="3" width="10" height="10" fill="none" stroke="#ffd200" stroke-width="1.5"/><path d="M4 7l3 3 8-9" stroke="#ffd200" stroke-width="2" fill="none"/></svg>Quality Work Guarantee</div>
  <div class="abs feature-box" style="top:1056px"><svg width="15" height="13" viewBox="0 0 16 14"><rect x="1" y="3" width="10" height="10" fill="none" stroke="#ffd200" stroke-width="1.5"/><path d="M4 7l3 3 8-9" stroke="#ffd200" stroke-width="2" fill="none"/></svg>24/7 Support</div>
  <div class="abs feature-box" style="top:1140px"><svg width="15" height="13" viewBox="0 0 16 14"><rect x="1" y="3" width="10" height="10" fill="none" stroke="#ffd200" stroke-width="1.5"/><path d="M4 7l3 3 8-9" stroke="#ffd200" stroke-width="2" fill="none"/></svg>Easy Installation</div>

  <div class="abs photo" style="left:653px;top:755px;width:178px;height:179px;background:linear-gradient(180deg,#8c9a74 0%,#e8e4dc 22%,#d9cdb7 100%)" role="img" aria-label="Living room with sofas and potted plant"></div>
  <div class="abs photo" style="left:653px;top:960px;width:178px;height:157px;background:linear-gradient(135deg,#e7e8ea,#9fa7b0)" role="img" aria-label="Technician servicing an indoor unit"></div>
  <div class="abs photo" style="left:848px;top:853px;width:179px;height:180px;background:linear-gradient(135deg,#6a5c4e,#c9ccd0 55%,#3a6ea5)" role="img" aria-label="Technician working on an outdoor condenser"></div>
  <div class="abs photo" style="left:848px;top:1048px;width:179px;height:180px;background:linear-gradient(135deg,#efe9df,#b9ad98)" role="img" aria-label="Couple relaxing in a living room"></div>
</section>

<!-- services -->
<section class="abs services">
  <div class="abs label">What we do</div>
  <div class="abs title">Our Premium Services</div>
  <div class="abs uline"></div>

  <div class="abs card" style="left:171px;top:201px"><div class="img" role="img" aria-label="Installer mounting an indoor unit"></div><div class="cap">Ductless Installation</div></div>
  <div class="abs card" style="left:392px;top:201px"><div class="img" role="img" aria-label="Hand opening an indoor unit cover"></div><div class="cap">Ductless Maintenance</div></div>
  <div class="abs card" style="left:612px;top:201px"><div class="img" role="img" aria-label="Technician repairing a circuit board"></div><div class="cap">Ductless Repairs</div></div>
  <div class="abs card" style="left:831px;top:201px"><div class="img" role="img" aria-label="Woman using a remote control"></div><div class="cap">Ductless Warranty</div></div>

  <div class="abs card" style="left:171px;top:379px"><div class="img" role="img" aria-label="Technician beside an indoor unit"></div><div class="cap">Ductless Remodels</div></div>
  <div class="abs card" style="left:392px;top:379px"><div class="img" role="img" aria-label="Open plan living room"></div><div class="cap">Whole House Ductless</div></div>
  <div class="abs card" style="left:612px;top:379px"><div class="img" role="img" aria-label="Technician checking an outdoor unit"></div><div class="cap">Heat Replacement</div></div>
  <div class="abs card" style="left:831px;top:379px"><div class="img" role="img" aria-label="Two outdoor condensers against a wall"></div><div class="cap">Single / Multi Zone<br>Ductless</div></div>

  <div class="abs more">VIEW MORE SERVICES</div>
</section>

<!-- why -->
<section>
  <div class="abs head-bar" style="left:171px;top:2045px">
    <div class="label">Why choose us</div>
    <div class="title">Why We Are The Best</div>
  </div>
  <p class="abs para" style="left:171px;top:2128px;width:470px">Quis autem vel eum iure reprehenderit qui in ea voluptate velit esse quam nihil molestiae consequatur, vel illum qui dolorem eum fugiat quo voluptas nulla pariatur</p>
  <div class="abs why-item" style="left:173px;top:2231px"><div class="sq-icon"><svg width="18" height="18" viewBox="0 0 20 20"><circle cx="10" cy="10" r="4" fill="#111"/><path d="M10 1v3M10 16v3M1 10h3M16 10h3M3.5 3.5l2 2M14.5 14.5l2 2M3.5 16.5l2-2M14.5 5.5l2-2" stroke="#111" stroke-width="1.6"/></svg></div>Great Technology</div>
  <div class="abs why-item" style="left:466px;top:2231px"><div class="sq-icon"><svg width="18" height="18" viewBox="0 0 20 20"><circle cx="10" cy="7" r="4" fill="#111"/><path d="M2 19c0-5 4-7 8-7s8 2 8 7z" fill="#111"/></svg></div>Certified engineers</div>
  <div class="abs why-item" style="left:173px;top:2283px"><div class="sq-icon"><svg width="18" height="18" viewBox="0 0 20 20"><circle cx="10" cy="11" r="7" fill="#111"/><path d="M10 7v8M8 9h3.5a1.5 1.5 0 0 1 0 3h-3" stroke="#ffd200" stroke-width="1.4" fill="none"/></svg></div>0% Financing for 48 months</div>
  <div class="abs why-item" style="left:466px;top:2283px"><div class="sq-icon"><svg width="18" height="18" viewBox="0 0 20 20"><circle cx="10" cy="10" r="8" fill="none" stroke="#111" stroke-width="2"/><circle cx="10" cy="10" r="5" fill="#111"/></svg></div>Money Back Guarantee</div>
  <div class="abs" style="left:701px;top:2042px;width:309px;height:292px;background:linear-gradient(135deg,#8a6a52 0%,#c9c6c2 35%,#2f2f33 70%,#f2c400 100%)" role="img" aria-label="Smiling technician in a hard hat beside an outdoor unit"></div>

  <!-- contact card -->
  <div class="abs contact-card">
    <h3>Contact Us Today</h3>
    <div class="abs c-row" style="top:100px"><div class="sq-icon"><svg width="11" height="15" viewBox="0 0 16 22"><path d="M8 0a8 8 0 0 0-8 8c0 6 8 14 8 14s8-8 8-14a8 8 0 0 0-8-8z" fill="#111"/><circle cx="8" cy="8" r="3" fill="#ffd200"/></svg></div>18 Larch Ave, Portland, USA</div>
    <div class="abs c-sep" style="top:171px"></div>
    <div class="abs c-row" style="top:191px"><div class="sq-icon"><svg width="14" height="11" viewBox="0 0 24 18"><rect x="1" y="1" width="22" height="16" fill="#111"/><path d="M1 1l11 9 11-9" stroke="#ffd200" stroke-width="2" fill="none"/></svg></div>info@tallfern.com</div>
    <div class="abs c-sep" style="top:262px"></div>
    <div class="abs c-row" style="top:289px"><div class="sq-icon"><svg width="13" height="13" viewBox="0 0 24 24"><path d="M6.6 10.8a15 15 0 0 0 6.6 6.6l2.2-2.2c.3-.3.7-.4 1-.2 1.1.4 2.3.6 3.6.6.6 0 1 .4 1 1V20c0 .6-.4 1-1 1A17 17 0 0 1 3 4c0-.6.4-1 1-1h3.5c.6 0 1 .4 1 1 0 1.3.2 2.5.6 3.6.1.3 0 .7-.2 1z" fill="#111"/></svg></div>000 - 000 - 000</div>
  </div>

  <!-- quote form -->
  <div class="abs quote">
    <h3 style="color:var(--yellow)">Request For Quote</h3>
    <div class="abs field" style="top:97px">Name...</div>
    <div class="abs field" style="top:135px">Phone Number...</div>
    <div class="abs field" style="top:172px">Email...</div>
    <div class="abs field" style="top:209px;height:123px;padding-top:14px">Message...</div>
    <div class="abs submit">SUBMIT</div>
  </div>

  <!-- promos -->
  <div class="abs promo" style="left:171px" role="img" aria-label="Family reviewing finances on a sofa"><div class="bar">Tall Fern Financing<span class="play"><svg width="10" height="12" viewBox="0 0 10 12"><path d="M0 0l10 6-10 6z" fill="#ffd200"/></svg></span></div></div>
  <div class="abs promo" style="left:466px;background:linear-gradient(135deg,#e8e8ea,#9a9ea6)" role="img" aria-label="Advisor meeting with a couple"><div class="bar">Tall Fern FAQ'S<span class="play"><svg width="10" height="12" viewBox="0 0 10 12"><path d="M0 0l10 6-10 6z" fill="#ffd200"/></svg></span></div></div>
  <div class="abs promo" style="left:758px;background:linear-gradient(135deg,#f3f1ec,#c6bba9)" role="img" aria-label="Family in a bright living room"><div class="bar">Tall Fern Blog<span class="play"><svg width="10" height="12" viewBox="0 0 10 12"><path d="M0 0l10 6-10 6z" fill="#ffd200"/></svg></span></div></div>
</section>

<!-- testimonials -->
<section class="abs testimonials">
  <div class="abs t-photo" role="img" aria-label="Portrait of a smiling client in a suit"><div class="fill"></div></div>
  <div class="abs head-bar" style="left:612px;top:99px">
    <div class="label">Testimonials</div>
    <div class="title">What Our Clients Say</div>
  </div>
  <p class="abs para" style="left:612px;top:209px;width:392px;font-size:12.5px;line-height:19px">Nam libero tempore, cum soluta nobis est eligendi optio cumque nihil impedit quo minus id quod maxime placeat facere possimus, omnis voluptas assumenda est, omnis dolor repellendus.</p>
  <div class="abs t-name"><i></i>Dana Whitlock</div>
  <div class="abs t-arrow" style="left:963px"><svg width="7" height="12" viewBox="0 0 7 12"><path d="M6 1L1 6l5 5" stroke="#ffd200" stroke-width="1.8" fill="none"/></svg></div>
  <div class="abs t-arrow" style="left:998px"><svg width="7" height="12" viewBox="0 0 7 12"><path d="M1 1l5 5-5 5" stroke="#ffd200" stroke-width="1.8" fill="none"/></svg></div>
</section>

<!-- footer -->
<footer class="abs footer">
  <div class="abs" style="left:200px;top:36px">
    <div class="brand"><span class="dot"></span><span class="name" style="color:var(--yellow)">Tall Fern Services</span></div>
    <div class="brand-sub" style="margin:7px 0 0 4px;color:var(--yellow)">DUCTLESS EXPERTS</div>
  </div>
  <p class="abs f-text" style="left:171px;top:117px;width:270px">Quis autem vel eum iure reprehenderit qui in ea voluptate velit esse quam nihil molestiae consequatur, vel illum qui dolorem eum fugiat quo voluptas nulla pariatur</p>
  <div class="abs f-social"><span></span><span></span><span></span><span></span></div>

  <h4 style="left:464px">Services</h4>
  <ul class="abs f-list" style="left:464px;top:116px"><li>Ductless Installation</li><li>Ductless Maintenance</li><li>Ductless Repairs</li><li>Ductless Warranty</li></ul>
  <ul class="abs f-list" style="left:630px;top:116px"><li>Remodels</li><li>Replacement</li><li>Ductless FAQ's</li><li>Ductless Home</li></ul>

  <h4 style="left:756px">Newsletter</h4>
  <p class="abs f-text" style="left:756px;top:119px;width:240px">Subscribe to our newsletter for latest updates</p>
  <div class="abs f-input">Email...</div>
  <div class="abs f-btn">SUBSCRIBE</div>
</footer>
<div class="abs copyright">©Copyright information here</div>

</body>
</html>
```